BRASKETT LAND SERVICES BILLBOARD DESIGN

I NEED A BILLBOARD FOR MY BUSINESS. WE ARE A LAND CLEARING COMPANY AND I WOULD LIKE TO ADD A PICTURE OF MY TRACK LOADER TO THE SIGN. OPEN TO COLORS. I WOULD ALSO LIKE TO HAVE MY PHONE NUMBER 555-284-7196, WEBSITE WWW.BRASKETTLANDSERVICES.EXAMPLE, AND EMAIL ON THE SIGN (CONTACT@BRASKETTLANDSERVICES.EXAMPLE). DESIGNERS CAN HAVE THE FREEDOM TO DO WHATEVER STYLE THEY WANT AND TO USE ANY COLORS THEY WANT.

Target Market(s)

ANYONE WITH PROPERTY

Requirements
Must have
• PICTURE OF TRACK LOADER, WEBSITE, PHONE NUMBER, EMAIL
Nice to have
• OPEN TO ANYTHING
Should not have
• OPEN TO ANYTHING

```html
<!DOCTYPE html>
<html lang="en">
<head>
<meta charset="utf-8">
<title>Braskett Land Services Billboard</title>
<link rel="stylesheet" href="https://fonts.googleapis.com/css2?family=Oswald:wght@500;600;700&display=swap">
<style>
  :root {
    --page-bg: #e6e6e4;
    --band-dark: #2b2724;
    --white: #ffffff;
    --accent-orange: #e2541f;
    --shadow-black: #111111;
    --photo-green: #4b5a2c;
    --photo-dark: #2f3a22;
    --photo-orange: #d8562a;
    --grass-light: #7ed43a;
    --grass-dark: #3f9a1c;
  }
  * { margin: 0; padding: 0; box-sizing: border-box; }
  html, body {
    width: 1058px;
    height: 1200px;
    overflow: hidden;
    background: var(--page-bg);
  }
  .billboard {
    position: absolute;
    left: 0;
    top: 335px;
    width: 1058px;
    height: 530px;
    overflow: hidden;
    background: var(--band-dark);
  }
  .machine-photo {
    position: absolute;
    left: 0; top: 0;
    width: 1058px;
    height: 322px;
    background:
      radial-gradient(ellipse at 20% 65%, rgba(216,86,42,0.75) 0%, rgba(216,86,42,0) 38%),
      radial-gradient(ellipse at 80% 65%, rgba(216,86,42,0.75) 0%, rgba(216,86,42,0) 38%),
      linear-gradient(180deg, var(--photo-dark) 0%, var(--photo-green) 55%, #6b6a3e 100%);
  }
  .torn-edge {
    position: absolute;
    left: 0; top: 304px;
    width: 1058px;
    height: 24px;
  }
  .brand-title {
    position: absolute;
    left: 0; top: 14px;
    width: 1058px;
    text-align: center;
    font-family: 'Oswald', sans-serif;
    font-weight: 600;
    font-size: 96px;
    line-height: 98px;
    color: var(--white);
    letter-spacing: 1px;
    text-shadow:
      2px 2px 0 var(--shadow-black), 4px 4px 0 var(--shadow-black),
      6px 6px 0 var(--shadow-black), 8px 8px 0 var(--shadow-black);
  }
  .brand-title span { display: block; }
  .contact-row {
    position: absolute;
    left: 18px; top: 368px;
    width: 1022px;
    height: 78px;
    display: flex;
    align-items: center;
  }
  .phone {
    font-family: 'Oswald', sans-serif;
    font-weight: 600;
    font-size: 86px;
    line-height: 1;
    color: var(--white);
    letter-spacing: 1px;
  }
  .divider {
    width: 4px;
    height: 78px;
    background: var(--accent-orange);
    margin: 0 18px 0 18px;
  }
  .online {
    flex: 1;
    text-align: right;
    font-family: 'Oswald', sans-serif;
    font-weight: 500;
    font-size: 25px;
    line-height: 32px;
    color: var(--white);
    letter-spacing: -0.2px;
  }
  .grass {
    position: absolute;
    left: 0; top: 478px;
    width: 1058px;
    height: 52px;
    background: linear-gradient(180deg, var(--grass-light) 0%, var(--grass-dark) 100%);
  }
</style>
</head>
<body>
  <section class="billboard">
    <div class="machine-photo" role="img" aria-label="Photo of two orange tracked loaders with forestry mulcher heads facing each other in front of trees"></div>
    <svg class="torn-edge" viewBox="0 0 1058 24" preserveAspectRatio="none" aria-hidden="true">
      <path fill="#ffffff" d="M0 8 L40 5 L80 9 L130 4 L170 8 L220 3 L260 7 L310 5 L360 9 L410 4 L460 8 L510 5 L560 9 L610 4 L660 7 L710 3 L760 8 L810 5 L860 9 L910 4 L960 8 L1010 5 L1058 7 L1058 16 L1020 19 L980 14 L940 18 L890 13 L850 17 L800 12 L750 18 L700 13 L650 17 L600 12 L550 18 L500 13 L450 16 L400 12 L350 18 L300 13 L250 17 L200 12 L150 18 L100 13 L60 17 L20 13 L0 16 Z"/>
    </svg>
    <h1 class="brand-title">
      <span>BRASKETT</span>
      <span>LAND</span>
      <span>SERVICES</span>
    </h1>
    <div class="contact-row">
      <div class="phone">555-284-7196</div>
      <div class="divider"></div>
      <div class="online">
        <div class="email">CONTACT@BRASKETTLANDSERVICES.EXAMPLE</div>
        <div class="website">WWW.BRASKETTLANDSERVICES.EXAMPLE</div>
      </div>
    </div>
    <div class="grass" role="img" aria-label="Illustrated strip of bright green grass"></div>
  </section>
</body>
</html>
```